Blog Banner Design Project: Notes For Wanderers

Looking for a new banner for my blog " Colin Ashworth's Notes for Wanderers" at http://www.notesforwanderers.example - and once design agreed also want an updated album art for the podcast that goes along with the site.
For more about the blog and what it is about:
http://www.notesforwanderers.example/about
Notes for Wanderers is a Luxury Travel Blog And Podcast that provides inspiration, advice and tips about luxurious travel experiences, including destinations, transportation, accommodation, and journeys, that travellers can read, listen to or watch.
Objective of the new design
(1) retain the colour scheme ideally to retain the brand identity, as have been using these colours since 2005.
(2) introduce more of my personality and make it more visually and overt that it is "Colin Ashworth's Notes for Wanderers", so possibly introducing my image into the blog banner so visitors are clear and more aware of the person behind the brand.
(3) needs to have an up-market, luxury but modern feel.
(4) if possible reflect the focus on the content (destinations, transportation, accommodation, attractions and journeys) - but this maybe best left to just words as want the design to be bold and more of the branding and personality.
Ideal wording
Smallish: Colin Ashworth's
Main wording: Notes for Wanderers
Sub-title/ small: luxurious destinations, transportation, accommodation and journeys.
Updates
I have a poll running with readers of my blog to rate the designs to help me to chose the final route, and so there is no need to submit any more designs. I will make the decision once the poll closes on the weekend.

```html
<!DOCTYPE html>
<html lang="en">
<head>
<meta charset="utf-8">
<title>Colin Ashworth's Notes for Wanderers – Blog Banner</title>
<link rel="stylesheet" href="https://fonts.googleapis.com/css2?family=Cormorant+Garamond:ital,wght@0,500;0,600;1,500&family=Montserrat:wght@500&display=swap">
<style>
  :root {
    --violet-deep: #3f2a6e;
    --violet: #6a4fa0;
    --violet-soft: #8a6fb8;
    --amber: #d99a3a;
    --gold: #f0b64a;
    --gold-pale: #f6d58e;
    --ink: rgba(20, 16, 30, 0.72);
    --ink-soft: rgba(20, 16, 30, 0.5);
    --white: #ffffff;
    --portrait-tone: #4b3d5a;
  }
  html, body {
    margin: 0;
    padding: 0;
    overflow: hidden;
    background: var(--white);
  }
  .banner {
    position: relative;
    width: 1200px;
    height: 202px;
    overflow: hidden;
  }
  .banner__backdrop {
    position: absolute;
    inset: 0;
    background: linear-gradient(90deg,
      var(--violet-deep) 0%,
      var(--violet) 30%,
      var(--violet-soft) 52%,
      #9c6f8a 66%,
      var(--amber) 82%,
      var(--gold) 100%);
  }
  .banner__portrait {
    position: absolute;
    left: 0;
    top: 0;
    width: 175px;
    height: 202px;
    background: linear-gradient(180deg, #6b5a7d 0%, var(--portrait-tone) 55%, #2e2836 100%);
  }
  .banner__panel {
    position: absolute;
    left: 286px;
    top: 14px;
    width: 690px;
    height: 138px;
    background: var(--ink);
    border-left: 4px solid var(--gold);
    box-sizing: border-box;
    padding: 14px 0 0 26px;
  }
  .banner__eyebrow {
    margin: 0;
    font-family: "Montserrat", sans-serif;
    font-weight: 500;
    font-size: 15px;
    line-height: 20px;
    letter-spacing: 5px;
    text-transform: uppercase;
    color: var(--gold-pale);
    white-space: nowrap;
  }
  .banner__title {
    margin: 4px 0 0;
    font-family: "Cormorant Garamond", serif;
    font-weight: 600;
    font-size: 72px;
    line-height: 84px;
    color: var(--white);
    white-space: nowrap;
  }
  .banner__tagline {
    position: absolute;
    right: 24px;
    top: 166px;
    margin: 0;
    padding: 0 14px;
    height: 28px;
    font-family: "Cormorant Garamond", serif;
    font-style: italic;
    font-weight: 500;
    font-size: 21px;
    line-height: 28px;
    color: var(--white);
    background: var(--ink-soft);
    white-space: nowrap;
  }
</style>
</head>
<body>
  <header class="banner">
    <div class="banner__backdrop" role="img" aria-label="Collage of travel scenes: a crowded beach, a waterfall, a harbour statue, city towers and an old road map, tinted from violet to gold"></div>
    <div class="banner__portrait" role="img" aria-label="Portrait photo of Colin Ashworth, the blogger"></div>

    <div class="banner__panel">
      <p class="banner__eyebrow">Colin Ashworth's</p>
      <h1 class="banner__title">Notes for Wanderers</h1>
    </div>

    <p class="banner__tagline">Luxurious destinations, transportation, accommodation and journeys.</p>
  </header>
</body>
</html>
```